African homeware retailer needs a web page design

We need a web page design for a new homeware and accessories store based in Johannesburg, South Africa. Our store carries modern African inspired items from designers that support social development and poverty alleviation initiatives. We have a particular preference for outfits that are centred on the empowerment of women.

Our business celebrates the skill, design and product of African craft and the work of designers looking to take that forward in a socially beneficial way (creating employment, developing skills, supporting local crafts people etc). We aim to carry items and inspirations from all over the African continent.

We would like to see a design that communicates African beauty and elegance without the typical tribal references that are made in reference to African craft or art.

We would like the web page to be stylish, uncomplicated, modern, captivating and appealing to the discerning customer. A similar value proposition is that of http://www.lindqvartworks.example/.

This is an e-commerce website which must be attractive to both individual buyers and design professionals so the website needs to look professional.

Here are links to some websites we like:
http://www.corvanhomes.example/
http://www.tesmoly.example/

Our logo is attached to the brief.

Target Market(s)

Our target market is female, age 20-50. However should not alienate the design conscious male customer therefore

Industry/Entity Type

E-Commerce

Requirements
Must have
• - A featured product banner which includes a photograph and text. This should be easy to edit as we will be changing the featured product regularly
- An easily expendable products section with categories. Examples of categories could be cushions, bedding, crockery etc. Should be easy to add new categories as well as new product pictures
- Home/landing page should be uncluttered
- Should use the logo and should be easy to change the logo which we have in various colour combinations. We plan to change the logo colours depending on circumstance e.g. make it red and white around Valentines day (similar to the way Zentrix frequently changes the logo on their landing page)

```html
<!DOCTYPE html>
<html lang="en">
<head>
<meta charset="utf-8">
<title>Zanolu Home – Home</title>
<link href="https://fonts.googleapis.com/css2?family=Arimo:wght@400;700&family=Montserrat:wght@400;600;700&family=Noto+Serif:wght@400&display=swap" rel="stylesheet">
<style>
:root{
  --orange:#e54e21;
  --orange-bright:#ff6a13;
  --teal:#1a7472;
  --header-bg:#f9f9f9;
  --text:#555;
  --text-dark:#2a2a2a;
  --line:#dedede;
  --banner-yellow:rgba(251,240,150,.85);
  --badge:#2b2b2b;
  --blue:#12b5ea;
  --green:#7fd321;
  --title-blue:#1ea0dc;
  --title-orange:#e4581f;
  --title-green:#3f8a2c;
  --footer-bg:#000;
  --footer-text:#a9a9a9;
}
*{margin:0;padding:0;box-sizing:border-box}
html,body{width:1200px;height:1000px;overflow:hidden;background:#fff}
body{position:relative;font-family:"Arimo",Arial,sans-serif;color:var(--text)}
.abs{position:absolute}
a{color:inherit;text-decoration:none}

/* header */
.site-header{left:0;top:0;width:1200px;height:175px;background:var(--header-bg)}
.brand{left:195px;top:96px;display:flex;align-items:center;gap:8px}
.brand-mark{width:14px;height:14px;background:var(--orange)}
.brand-name{font-family:"Montserrat",sans-serif;font-weight:600;font-size:17px;letter-spacing:1.5px;color:var(--orange);text-transform:uppercase}
.welcome{left:683px;top:44px;font-family:"Montserrat",sans-serif;font-size:8.5px;font-weight:600;color:#777;font-variant:small-caps;letter-spacing:0}
.welcome a{color:var(--orange);font-size:9.5px}
.search{left:683px;top:69px;width:156px;height:29px;display:flex;border:1px solid #e2e2e2;background:#fff}
.search span{flex:1;font-size:7px;color:#bbb;padding:10px 9px;letter-spacing:.5px}
.search-btn{width:32px;height:29px;margin:-1px -1px 0 0;background:var(--orange);display:flex;align-items:center;justify-content:center}
.cart{left:857px;top:69px;width:156px;height:29px;border:1px solid #e2e2e2;background:#fff;display:flex}
.cart span{flex:1;font-family:"Montserrat",sans-serif;font-weight:600;font-size:9.5px;color:#888;padding:8px 7px;font-variant:small-caps;white-space:nowrap}
.cart-toggle{width:31px;border-left:1px solid #e2e2e2;display:flex;align-items:center;justify-content:center}
.util-nav{left:480px;top:115px;font-size:7px;color:#555;white-space:nowrap}
.util-nav i{font-style:normal;margin:0 3px}
.header-rule{left:480px;top:137px;width:532px;height:1px;background:var(--line)}
.main-nav a{position:absolute;top:149px;font-family:"Montserrat",sans-serif;font-weight:700;font-size:9.6px;color:var(--teal);white-space:nowrap}

/* hero */
.hero-photo-a{left:258px;top:258px;width:175px;height:102px;border-radius:50% 50% 8px 8px;background:linear-gradient(135deg,#f4f4f4,#cfcfcf)}
.hero-photo-b{left:515px;top:278px;width:355px;height:82px;border-radius:40px 40px 6px 6px;background:linear-gradient(180deg,#eef0f6,#d8dbe6)}
.banner{left:194px;top:357px;width:818px;height:89px;background:var(--banner-yellow)}
.banner h1{position:absolute;left:90px;top:16px;font-family:"Montserrat",sans-serif;font-weight:700;font-size:32px;color:var(--text-dark);letter-spacing:1.2px}
.banner p{position:absolute;left:93px;top:51px;font-size:14.5px;color:var(--text-dark)}
.btn-shop{position:absolute;left:651px;top:28px;width:95px;height:34px;background:var(--orange);color:#fff;font-family:"Montserrat",sans-serif;font-weight:700;font-size:12px;display:flex;align-items:center;justify-content:center}
.save-badge{left:842px;top:239px;width:98px;height:98px;border-radius:50%;background:var(--badge);color:#fff;text-align:center;padding-top:26px;font-size:10px;line-height:1.1}
.save-badge b{font-weight:400;font-size:12px}
.save-badge big{font-size:24px}
.hero-rule{left:194px;top:461px;width:818px;height:1px;background:var(--line)}

/* feature cards */
.divider-v{top:495px;width:1px;height:168px;background:var(--line)}
.feature-photo{width:80px;height:70px;border-radius:6px}
.feature-title{font-family:"Noto Serif",serif;font-weight:400;font-size:16px;white-space:nowrap}
.feature-text{font-size:8.5px;line-height:1.45;color:#555;width:145px}
.btn{height:28px;color:#fff;font-family:"Montserrat",sans-serif;font-weight:700;font-size:10px;display:flex;align-items:center;justify-content:center}

/* info strip */
.info-strip{left:0;top:699px;width:1200px;height:54px;background:#f7f7f7;border-top:1px solid var(--line)}
.follow{left:194px;top:718px;font-family:"Montserrat",sans-serif;font-weight:600;font-size:16.5px;color:#6b6b6b}
.social{top:714px;width:28px;height:28px;background:#3a3a3a}
.strip-div{top:712px;width:1px;height:31px;background:var(--line)}
.ship-title{left:509px;top:714px;font-family:"Montserrat",sans-serif;font-weight:700;font-size:11.5px;color:var(--orange)}
.ship-sub{left:509px;top:727px;font-family:"Montserrat",sans-serif;font-weight:600;font-size:9.5px;color:#777;font-variant:small-caps;white-space:nowrap}
.order{left:779px;top:720px;font-family:"Montserrat",sans-serif;font-weight:600;font-size:12px;color:#6b6b6b;white-space:nowrap}
.order b{color:var(--orange);margin-left:2px;font-size:12.5px;font-weight:600}

/* footer */
.site-footer{left:0;top:753px;width:1200px;height:200px;background:var(--footer-bg)}
.footer-col{top:797px}
.footer-col h4{font-family:"Montserrat",sans-serif;font-weight:600;font-size:9.5px;color:#ddd;margin-bottom:9px;letter-spacing:.3px}
.footer-col li{list-style:none;font-size:8px;color:var(--footer-text);line-height:15.7px}
.newsletter{left:823px;top:820px;width:190px;height:26px;display:flex}
.newsletter span{flex:1;background:#3d3d3d;color:#999;font-size:7px;padding:9px 7px}
.newsletter b{width:45px;background:var(--orange);color:#fff;font-size:10px;display:flex;align-items:center;justify-content:center}
.store{left:823px;top:863px;font-size:8px;line-height:13px;color:var(--footer-text)}
.legal-bar{left:0;top:953px;width:1200px;height:47px;background:var(--orange);color:#fff;font-family:"Montserrat",sans-serif;font-weight:600;font-size:8px;font-variant:small-caps}
.legal-bar .copy{position:absolute;left:194px;top:18px}
.legal-bar .links{position:absolute;right:188px;top:18px}
</style>
</head>
<body>

<header class="abs site-header"></header>
<div class="abs brand"><span class="brand-mark"></span><span class="brand-name">Zanolu Home</span></div>
<p class="abs welcome">Welcome visitor you can <a href="#">Login</a> or <a href="#">Create an Account</a></p>
<div class="abs search"><span>SEARCH</span><div class="search-btn">
  <svg width="12" height="12" viewBox="0 0 12 12"><circle cx="5" cy="5" r="3.5" fill="none" stroke="#fff" stroke-width="1.6"/><line x1="7.5" y1="7.5" x2="11" y2="11" stroke="#fff" stroke-width="1.8"/></svg>
</div></div>
<div class="abs cart"><span>Cart 0 item(s) - $0.00</span><div class="cart-toggle">
  <svg width="11" height="6" viewBox="0 0 11 6"><polyline points="0.5,0.5 5.5,5 10.5,0.5" fill="none" stroke="#aaa"/></svg>
</div></div>
<nav class="abs util-nav">HOME<i>|</i>WISH LIST (0)<i>|</i>MY ACCOUNT<i>|</i>SHOPPING CART<i>|</i>CHECKOUT</nav>
<div class="abs header-rule"></div>
<nav class="main-nav">
  <a href="#" style="left:480px">LOREM IPSUM</a>
  <a href="#" style="left:578px">LOREM IPSUM</a>
  <a href="#" style="left:670px">LOREM IPSUM</a>
  <a href="#" style="left:762px">LOREM IPSUM</a>
  <a href="#" style="left:860px">LOREM IPSUM</a>
</nav>

<div class="abs hero-photo-a" role="img" aria-label="Black and white patterned crockery set"></div>
<div class="abs hero-photo-b" role="img" aria-label="White dinner set with blue rims and floral detail"></div>
<section class="abs banner">
  <h1>CROCKERY</h1>
  <p>A Large Selection At Competitive Price</p>
  <a class="btn-shop" href="#">SHOP NOW!</a>
</section>
<div class="abs save-badge"><b>SAVE</b> <big>25%</big><br>On Selected<br>Products</div>
<div class="abs hero-rule"></div>

<div class="abs divider-v" style="left:469px"></div>
<div class="abs divider-v" style="left:750px"></div>

<div class="abs feature-photo" role="img" aria-label="Stack of colourful striped cushions" style="left:195px;top:528px;background:linear-gradient(135deg,#2d6fb8,#e8b52a 45%,#c23b2a)"></div>
<h3 class="abs feature-title" style="left:310px;top:528px;color:var(--title-blue)">Home Appliance</h3>
<p class="abs feature-text" style="left:311px;top:561px">Lorem ipsum dolor sit amet, consect-etur adipisicing elit, sed do eiusmod</p>
<a class="abs btn" href="#" style="left:313px;top:613px;width:88px;background:var(--blue)">LEARN MORE</a>

<div class="abs feature-photo" role="img" aria-label="Bed made with grey patterned bedding" style="left:497px;top:532px;background:linear-gradient(180deg,#5a5350,#9b959a 50%,#6f6a70)"></div>
<h3 class="abs feature-title" style="left:586px;top:528px;color:var(--title-orange)">Special Offer</h3>
<p class="abs feature-text" style="left:587px;top:561px">Lorem ipsum dolor sit amet, consect-etur adipisicing elit, sed do eiusmod tempor</p>
<a class="abs btn" href="#" style="left:588px;top:613px;width:90px;background:var(--orange-bright)">VIEW DETAIL</a>

<div class="abs feature-photo" role="img" aria-label="White crockery set with dark pattern" style="left:768px;top:528px;width:98px;background:linear-gradient(135deg,#f2f2f2,#bdbdbd)"></div>
<h3 class="abs feature-title" style="left:869px;top:528px;color:var(--title-green)">Free Shipping</h3>
<p class="abs feature-text" style="left:870px;top:561px;width:140px">on selected lorem ipsum products &amp; home appliance</p>
<a class="abs btn" href="#" style="left:872px;top:613px;width:89px;background:var(--green)">READ MORE</a>

<section class="abs info-strip"></section>
<p class="abs follow">FOLLOW US</p>
<a class="abs social" href="#" aria-label="Social profile one" style="left:326px"></a>
<a class="abs social" href="#" aria-label="Social profile two" style="left:360px"></a>
<div class="abs strip-div" style="left:468px"></div>
<p class="abs ship-title">FREE SHIPPING</p>
<p class="abs ship-sub">SHIPPING COST: On Order over $99</p>
<div class="abs strip-div" style="left:750px"></div>
<p class="abs order">ORDER ONLINE <b>TEL: 1234 5678 001</b></p>

<footer class="abs site-footer"></footer>
<div class="abs footer-col" style="left:194px"><h4>MY ACCOUNT</h4><ul><li>Sign In</li><li>View Cart</li><li>My Wishlist</li><li>Track My Order</li><li>Help</li></ul></div>
<div class="abs footer-col" style="left:418px"><h4>SITE INFO</h4><ul><li>About Us</li><li>Customer Service</li><li>Privacy Policy</li><li>Site Map</li><li>Search Terms</li><li>Advanced Search</li><li>Orders and Returns</li></ul></div>
<div class="abs footer-col" style="left:621px"><h4>WHY BUY FOR US</h4><ul><li>Shipping &amp; Returns</li><li>Secure Shopping</li><li>International Shipping</li><li>Affiliates</li><li>Group Sales</li><li>Contact Us</li></ul></div>
<div class="abs footer-col" style="left:823px"><h4>NEWSLETTER</h4></div>
<div class="abs newsletter"><span>Enter Your Email Address</span><b>Go</b></div>
<p class="abs store">Store Location: #1234, Lorem Ipsum Link<br>Lorem Ipsum, 2345</p>

<div class="abs legal-bar">
  <span class="copy">© 2014 Company Name. All Rights Reserved</span>
  <span class="links">Privacy Policy &nbsp;|&nbsp; Terms &amp; Conditions</span>
</div>

</body>
</html>
```